Whimsical Flyer for Children's Storytime at Glow And Grow

Design an 8 1/2 by 11 color flyer to promote a storytime series at our store. At Glow And Grow we believe that the shortest distance between two people is a story. Everything in our store has a story behind it and now we are excited to have one of the world’s best storytellers coming to share her gifts with kids ages 2-5, once a week, starting at 10am on July 7th for an eight-week series. Ms. Dolores (Pemberley), children’s librarian and storyteller extraordinaire, and our own Mr. Toby, her budding apprentice, will regale children with music, stories and movement, FREE! 10am. Reservations required. Visit glowandgrow.example for details. 872 E. 61st Street - San Mateo CA 94417.

Target Market(s)

Parents and caregivers with children

Requirements
Must have
• Whimsy, fun, enticing to parents and children

```html
<!DOCTYPE html>
<html lang="en">
<head>
<meta charset="utf-8">
<title>Welcome to Storytime – Glow And Grow</title>
<link rel="stylesheet" href="https://fonts.googleapis.com/css2?family=Lilita+One&family=Arimo:wght@400;700&family=Open+Sans:wght@400;600;700&display=swap">
<style>
  :root {
    --backdrop: #444444;
    --paper: #ffffff;
    --teal: #16a09a;
    --teal-dark: #0f8580;
    --yellow: #f3e24b;
    --orange: #e66c24;
    --orange-bright: #f07a2a;
    --brown: #4a2410;
    --brown-mid: #8a4b24;
    --olive: #7d8a2c;
    --grey-bg: #ececec;
    --ink: #333333;
    --outline: #7a3a12;
  }
  * { box-sizing: border-box; margin: 0; padding: 0; }
  html, body { width: 1200px; height: 1200px; overflow: hidden; background: var(--backdrop); }
  .stage { width: 1100px; height: 1100px; transform: scale(1.090909); transform-origin: 0 0; position: relative; }
  .flyer {
    position: absolute; left: 196px; top: 65px; width: 745px; height: 963px;
    background: var(--grey-bg); overflow: hidden; font-family: "Open Sans", Arial, sans-serif;
  }
  .abs { position: absolute; }
  .backdrop-shapes { left: 0; top: 0; }

  .hero-photo {
    left: 330px; top: 0; width: 415px; height: 390px;
    background: linear-gradient(135deg, #f4f4f2 0%, #e9e6e2 45%, #d9c6b4 100%);
  }
  .brand { left: 14px; top: 14px; display: flex; align-items: center; gap: 12px; }
  .brand-dot { width: 40px; height: 40px; border-radius: 50%; background: var(--orange); }
  .brand-name { font-family: "Open Sans", Arial, sans-serif; font-weight: 700; font-size: 26px; color: var(--brown-mid); letter-spacing: 0.5px; }

  .headline {
    left: 22px; top: 150px; width: 440px; font-family: "Lilita One", "Arial Rounded MT Bold", sans-serif;
    line-height: 0.95; transform: rotate(-4deg); transform-origin: left center;
  }
  .headline span { display: block; -webkit-text-stroke: 3px var(--outline); paint-order: stroke fill; text-shadow: 0 4px 0 rgba(90,40,10,0.35); }
  .headline .line-one { font-size: 70px; color: var(--yellow); }
  .headline .line-two { font-size: 80px; color: var(--orange-bright); margin-left: 68px; }

  .tagline {
    left: 100px; top: 333px; width: 440px; text-align: center; color: #fff;
    font-family: "Arimo", Arial, sans-serif; font-weight: 700; font-size: 20px; line-height: 22px;
  }
  .tagline u { text-underline-offset: 3px; }

  .price-badge {
    left: 540px; top: 250px; width: 192px; height: 192px; border-radius: 50%;
    background: var(--orange); border: 7px solid #fff;
    display: flex; flex-direction: column; align-items: center; justify-content: center;
    box-shadow: 0 2px 6px rgba(0,0,0,0.15);
  }
  .price-badge .free { font-family: "Arimo", Arial, sans-serif; font-weight: 700; font-size: 64px; color: var(--yellow); line-height: 1; transform: scaleX(0.85); }
  .price-badge .time { font-family: "Arimo", Arial, sans-serif; font-weight: 700; font-size: 22px; color: #fff; margin-top: 4px; }

  .intro {
    left: 20px; top: 446px; width: 705px; text-align: center; color: var(--ink);
    font-size: 14.5px; line-height: 20px;
  }

  .calendar-icon { left: 188px; top: 496px; }
  .schedule-box {
    left: 250px; top: 494px; width: 363px; height: 56px; border-radius: 6px; background: var(--brown-mid);
    color: #fff; font-weight: 700; font-size: 17.5px; line-height: 22px; text-align: center; padding-top: 6px;
  }

  .storyteller-photo {
    left: 0; top: 530px; width: 345px; height: 372px;
    background: linear-gradient(160deg, #f2e36a 0%, #e8d6c6 40%, #c98d6a 75%, #6b8a3a 100%);
  }
  .book-scene {
    left: 345px; top: 495px; width: 400px; height: 225px;
    background: linear-gradient(180deg, #f3f3f3 0%, #dcdcdc 60%, #9a6a44 78%, #7a4e2c 100%);
  }

  .program-band { left: 345px; top: 720px; width: 400px; height: 145px; background: var(--brown); }
  .program-icons { left: 0; top: 12px; width: 400px; display: flex; justify-content: center; gap: 12px; }
  .program-icon { width: 58px; height: 58px; border-radius: 50%; border: 2px solid #fff; display: flex; align-items: center; justify-content: center; }
  .program-icon.music { background: var(--olive); }
  .program-icon.story { background: var(--orange); }
  .program-icon.move { background: var(--brown-mid); }
  .program-text {
    left: 14px; top: 82px; width: 372px; text-align: center; color: #fff; font-weight: 600; font-size: 14px; line-height: 20px;
  }
  .activity-bar {
    left: 345px; top: 865px; width: 400px; height: 36px; background: var(--orange);
    color: #fff; font-family: "Arimo", Arial, sans-serif; font-weight: 700; font-size: 21px;
    display: flex; align-items: center; justify-content: center; letter-spacing: 0.3px;
  }

  .footer { left: 0; top: 901px; width: 745px; height: 62px; background: var(--paper); }
  .reservation-pill {
    left: 14px; top: 14px; width: 338px; height: 36px; border-radius: 0 18px 18px 0; background: var(--teal);
    color: #fff; font-weight: 700; font-size: 20px; display: flex; align-items: center; justify-content: center;
  }
  .contact {
    left: 370px; top: 12px; width: 370px; text-align: center; font-family: "Arimo", Arial, sans-serif;
    font-weight: 700; font-size: 16.5px; line-height: 20px; color: #111;
  }
  .contact .web { color: var(--orange); }
</style>
</head>
<body>
<div class="stage">
  <main class="flyer">
    <div class="abs hero-photo" role="img" aria-label="Photo of a smiling young girl resting her chin on her hand"></div>

    <svg class="abs backdrop-shapes" width="745" height="470" viewBox="0 0 745 470" aria-hidden="true">
      <path d="M0 120 C120 60 260 80 330 120 L330 0 L0 0 Z" fill="#fff"/>
      <path d="M0 125 C140 40 300 70 390 200 C460 300 560 360 745 330 L745 345 C560 390 440 330 380 250 C300 120 150 80 0 150 Z" fill="var(--yellow)"/>
      <path d="M0 150 C150 80 300 120 380 250 C440 340 540 380 640 372 L600 440 C480 450 300 440 0 420 Z" fill="var(--teal)"/>
      <path d="M0 0 L300 0 C220 90 110 110 0 105 Z" fill="#fff"/>
      <path d="M0 105 C110 110 220 90 300 0 L312 0 C230 100 110 122 0 118 Z" fill="#7fcfca"/>
      <path d="M0 420 C200 445 430 450 600 440 L745 440 L745 470 L0 470 Z" fill="var(--grey-bg)"/>
    </svg>

    <div class="abs brand">
      <span class="brand-dot"></span>
      <span class="brand-name">Glow And Grow</span>
    </div>

    <h1 class="abs headline">
      <span class="line-one">Welcome to</span>
      <span class="line-two">Storytime!</span>
    </h1>

    <p class="abs tagline">At Glow And Grow ,<br>we believe that the shortest distance<br>between two people is <u>a story. </u></p>

    <div class="abs price-badge">
      <span class="free">FREE</span>
      <span class="time">10 AM</span>
    </div>

    <p class="abs intro">Everything in our store has a story behind it and now we are excited to have one of the world’s<br>best storytellers coming to share her gifts with <strong>kids ages 2-5</strong></p>

    <div class="abs book-scene" role="img" aria-label="Illustration of an open book on a wooden table with a palm tree, a ship and letters rising from its pages"></div>

    <div class="abs storyteller-photo" role="img" aria-label="Photo of the storyteller holding a picture book, a frog puppet and a toy train"></div>

    <svg class="abs calendar-icon" width="52" height="52" viewBox="0 0 52 52" aria-hidden="true">
      <rect x="3" y="7" width="46" height="42" rx="5" fill="none" stroke="var(--orange)" stroke-width="3"/>
      <rect x="3" y="7" width="46" height="10" rx="4" fill="var(--orange)"/>
      <rect x="13" y="2" width="4" height="10" rx="2" fill="var(--orange)"/>
      <rect x="35" y="2" width="4" height="10" rx="2" fill="var(--orange)"/>
      <g fill="var(--orange)">
        <rect x="10" y="22" width="6" height="5"/><rect x="19" y="22" width="6" height="5"/><rect x="28" y="22" width="6" height="5"/><rect x="37" y="22" width="6" height="5"/>
        <rect x="10" y="31" width="6" height="5"/><rect x="19" y="31" width="6" height="5"/><rect x="28" y="31" width="6" height="5"/><rect x="37" y="31" width="6" height="5"/>
        <rect x="10" y="40" width="6" height="5"/><rect x="19" y="40" width="6" height="5"/><rect x="28" y="40" width="6" height="5"/>
      </g>
    </svg>
    <div class="abs schedule-box">STARTING at 10am on July 7th<br>once a week,for an eight-week series.</div>

    <section class="abs program-band">
      <div class="abs program-icons">
        <span class="program-icon music">
          <svg width="32" height="32" viewBox="0 0 32 32" aria-hidden="true"><path d="M11 24 V8 L26 5 V21" fill="none" stroke="#fff" stroke-width="2.5"/><ellipse cx="8" cy="24" rx="4" ry="3" fill="#fff"/><ellipse cx="23" cy="21" rx="4" ry="3" fill="#fff"/></svg>
        </span>
        <span class="program-icon story">
          <svg width="34" height="30" viewBox="0 0 34 30" aria-hidden="true"><path d="M17 6 C12 3 6 3 2 5 V26 C6 24 12 24 17 27 C22 24 28 24 32 26 V5 C28 3 22 3 17 6 Z M17 6 V27" fill="none" stroke="#fff" stroke-width="2.5" stroke-linejoin="round"/></svg>
        </span>
        <span class="program-icon move">
          <svg width="32" height="32" viewBox="0 0 32 32" aria-hidden="true"><path d="M6 10 Q11 5 16 10 T26 10 M6 17 Q11 12 16 17 T26 17 M6 24 Q11 19 16 24 T26 24" fill="none" stroke="#fff" stroke-width="2.5" stroke-linecap="round"/></svg>
        </span>
      </div>
      <p class="abs program-text">Ms. Dolores (Pemberley), children’s librarian and storyteller extraordinaire, and our own Mr. Toby, her budding apprentice, will regale children with</p>
    </section>
    <div class="abs activity-bar">MUSIC - STORIES - MOVEMENT</div>

    <footer class="abs footer">
      <div class="abs reservation-pill">RESERVATIONS REQUIRED</div>
      <p class="abs contact">Visit <span class="web">glowandgrow.example</span> for details.<br>872 E. 61st Street - San Mateo CA 94417</p>
    </footer>
  </main>
</div>
</body>
</html>
```